Silver Birch Decorators Banner

Create a banner that displays and reinforces Silver Birch Decorators’ brand identity while promoting our interior painting services. The banner will be displayed at indoor venues through the winter. The design should be clean, professional, and visually recognizable to both new and returning customers. See attached design brief & logo source files.

```html
<!DOCTYPE html>
<html lang="en">
<head>
<meta charset="utf-8">
<title>Silver Birch Decorators – Interior Painting Banner</title>
<link rel="stylesheet" href="https://fonts.googleapis.com/css2?family=Michroma&family=Montserrat:wght@700;800&family=Roboto+Condensed:wght@700&display=swap">
<style>
  :root {
    --brand-green: #6b8f4e;
    --charcoal: #474747;
    --ink: #3a3a3a;
    --paper: #ffffff;
    --backdrop: #e9eaec;
  }
  * { margin: 0; padding: 0; box-sizing: border-box; }
  html, body {
    width: 1200px;
    height: 879px;
    overflow: hidden;
    background: var(--backdrop);
  }
  .banner {
    position: absolute;
    left: 0;
    top: 257px;
    width: 1200px;
    height: 364px;
    background: var(--paper);
    overflow: hidden;
  }
  .banner-shapes {
    position: absolute;
    inset: 0;
    width: 1200px;
    height: 364px;
  }
  .brand {
    position: absolute;
    left: 36px;
    top: 30px;
    display: flex;
    align-items: center;
    gap: 18px;
  }
  .brand-square {
    width: 30px;
    height: 30px;
    background: var(--charcoal);
  }
  .brand-name {
    font-family: "Montserrat", sans-serif;
    font-weight: 800;
    font-size: 50px;
    line-height: 1;
    color: var(--brand-green);
    text-transform: uppercase;
  }
  .headline {
    position: absolute;
    left: 668px;
    top: 4px;
    width: 450px;
    text-align: center;
    font-family: "Michroma", sans-serif;
    font-size: 44px;
    line-height: 54px;
    letter-spacing: 3px;
    color: var(--paper);
    text-transform: uppercase;
  }
  .tagline {
    position: absolute;
    left: 0;
    top: 190px;
    width: 1200px;
    text-align: center;
    font-family: "Montserrat", sans-serif;
    font-weight: 700;
    font-size: 24px;
    color: var(--ink);
  }
  .services {
    position: absolute;
    left: 0;
    top: 245px;
    width: 1200px;
    text-align: center;
    font-family: "Montserrat", sans-serif;
    font-weight: 700;
    font-size: 29px;
    letter-spacing: 0.5px;
    color: var(--brand-green);
  }
  .cta {
    position: absolute;
    left: 18px;
    top: 316px;
    font-family: "Roboto Condensed", sans-serif;
    font-weight: 700;
    font-size: 31px;
    color: var(--paper);
  }
  .web {
    position: absolute;
    left: 760px;
    top: 322px;
    width: 420px;
    text-align: center;
    font-family: "Montserrat", sans-serif;
    font-weight: 700;
    font-size: 29px;
    color: var(--paper);
  }
</style>
</head>
<body>
  <section class="banner">
    <svg class="banner-shapes" viewBox="0 0 1200 364" aria-hidden="true">
      <polygon class="accent-stripe" points="574,0 597,0 676,165 653,165" fill="var(--brand-green)"/>
      <polygon class="headline-panel" points="597,0 1200,0 1200,165 676,165" fill="var(--charcoal)"/>
      <polygon class="cta-bar" points="0,310 698,310 728,364 0,364" fill="var(--charcoal)"/>
      <polygon class="web-bar" points="718,318 1200,318 1200,364 744,364" fill="var(--brand-green)"/>
    </svg>

    <div class="brand">
      <span class="brand-square"></span>
      <p class="brand-name">Silver Birch<br>Decorators</p>
    </div>

    <h1 class="headline">Interior<br>Painting<br>Services</h1>

    <p class="tagline">Paint Smarter" "Trusted local professionals, since 2005"</p>

    <p class="services">Walls • Ceilings • Trim • Cabinets • Drywall Repair</p>

    <p class="cta">Call to action: “Book a Free Estimate at</p>
    <p class="web">www.silverbirchdeco.com</p>
  </section>
</body>
</html>
```